Ward Compass Business Card Design*

We need a business card design for our company Ward Compass. Our company is specialized in providing online consulting services regarding medical institutions, hospitals and doctors. We work with patients worldwide looking to choose between healthcare providers. We have a website you may use as a reference, where we list doctors and clinics worldwide. So we target Medical providers as well as patients worldwide.
Target Market(s)
Medical Providers and patients around the world
Industry/Entity Type
Medical
Contact Information for Business Card
Salma Driouch
CEO
+90 612 348 2751
info@wardcompass.example
www.wardcompass.example
17 Essafsaf 3 H.Q.L. Rabat, Morocco
Requirements
Must have
- Company logo/name on one full side, personal info and smaller logo and company name on the other side.
Nice to have
- Smart and elegant design

```html
<!DOCTYPE html>
<html lang="en">
<head>
<meta charset="utf-8">
<title>Ward Compass Business Card</title>
<link rel="stylesheet" href="https://fonts.googleapis.com/css2?family=Roboto:wght@400;500;700&display=swap">
<style>
  :root {
    --page-bg: #e9e6e2;
    --navy-deep: #0d1526;
    --navy-mid: #1f2d46;
    --navy-soft: #2b3a55;
    --frost-light: #f3f4f6;
    --frost-mid: #d9dde3;
    --curve-shadow: #4a4f58;
    --text-light: #e6e6e6;
    --text-muted: #cfd2d8;
    --icon-tan: #c9b8a6;
    --logo-ink: #1b2230;
  }
  * { margin: 0; padding: 0; box-sizing: border-box; }
  html, body {
    width: 1200px; height: 970px; overflow: hidden;
    background: var(--page-bg);
    font-family: "Roboto", Arial, sans-serif;
  }
  .business-card {
    position: absolute; left: 100px; top: 200px;
    width: 1000px; height: 569px;
    border-radius: 30px; overflow: hidden;
    box-shadow: 0 20px 50px rgba(0,0,0,0.25);
  }
  .card-surface { position: absolute; inset: 0; width: 100%; height: 100%; }
  .brand-lockup {
    position: absolute; left: 560px; top: 84px;
    display: flex; align-items: center; gap: 16px;
  }
  .brand-mark {
    width: 66px; height: 66px; border-radius: 50%;
    border: 9px solid var(--logo-ink);
  }
  .brand-name {
    font-size: 36px; font-weight: 500; letter-spacing: 1px;
    color: var(--logo-ink); text-transform: uppercase;
  }
  .holder {
    position: absolute; left: 47px; top: 288px; color: var(--text-light);
  }
  .holder-name { font-size: 31px; font-weight: 400; letter-spacing: 0.5px; }
  .holder-name strong { font-weight: 500; }
  .holder-role { font-size: 23px; color: var(--text-muted); margin-top: 4px; }
  .contact-list {
    position: absolute; left: 47px; top: 418px; list-style: none;
  }
  .contact-item {
    display: flex; align-items: center; gap: 17px;
    height: 36px; font-size: 23px; color: var(--text-muted);
  }
  .contact-icon { width: 26px; height: 26px; flex: none; }
  .social-links {
    position: absolute; left: 796px; top: 476px;
    display: flex; gap: 18px;
  }
  .social-slot {
    width: 33px; height: 33px; border-radius: 3px;
    background: var(--frost-mid);
  }
</style>
</head>
<body>
  <div class="business-card">
    <svg class="card-surface" viewBox="0 0 1000 569" preserveAspectRatio="none" aria-hidden="true">
      <defs>
        <linearGradient id="frost" x1="0" y1="0" x2="1" y2="1">
          <stop offset="0" stop-color="#e4e6ea"/>
          <stop offset="0.5" stop-color="#f6f7f9"/>
          <stop offset="1" stop-color="#dcdfe4"/>
        </linearGradient>
        <radialGradient id="navy" cx="0.3" cy="0.4" r="0.8">
          <stop offset="0" stop-color="#2a3956"/>
          <stop offset="0.6" stop-color="#18233a"/>
          <stop offset="1" stop-color="#0c1322"/>
        </radialGradient>
      </defs>
      <rect width="1000" height="569" fill="url(#frost)"/>
      <path class="curve-shadow" d="M395 0 C430 170 560 240 700 300 C840 360 960 390 1000 460 L1000 569 L0 569 L0 0 Z" fill="#4a4f58"/>
      <path class="navy-field" d="M375 0 C405 175 540 250 690 310 C830 366 950 405 1000 478 L1000 569 L0 569 L0 0 Z" fill="url(#navy)"/>
    </svg>

    <div class="brand-lockup">
      <span class="brand-mark"></span>
      <span class="brand-name">Ward Compass</span>
    </div>

    <div class="holder">
      <p class="holder-name"><strong>SALMA</strong> DRIOUCH</p>
      <p class="holder-role">CEO</p>
    </div>

    <ul class="contact-list">
      <li class="contact-item">
        <svg class="contact-icon" viewBox="0 0 26 26"><circle cx="13" cy="13" r="13" fill="#c9b8a6"/><path d="M9 7 L11 7 L12 10 L10.5 11.5 C11.3 13.3 12.7 14.7 14.5 15.5 L16 14 L19 15 L19 17 C19 18 18 19 17 19 C11.5 18.5 7.5 14.5 7 9 C7 8 8 7 9 7 Z" fill="#1f2d46"/></svg>
        +90 612 348 2751
      </li>
      <li class="contact-item">
        <svg class="contact-icon" viewBox="0 0 26 26"><circle cx="13" cy="13" r="13" fill="#c9b8a6"/><rect x="7" y="8.5" width="12" height="9" fill="#1f2d46"/><path d="M7 8.5 L13 13.5 L19 8.5" fill="none" stroke="#c9b8a6" stroke-width="1.4"/></svg>
        info@wardcompass.example
      </li>
      <li class="contact-item">
        <svg class="contact-icon" viewBox="0 0 26 26"><circle cx="13" cy="13" r="13" fill="#c9b8a6"/><g fill="none" stroke="#1f2d46" stroke-width="1.5"><circle cx="13" cy="13" r="6.5"/><ellipse cx="13" cy="13" rx="3" ry="6.5"/><line x1="6.5" y1="13" x2="19.5" y2="13"/></g></svg>
        www.wardcompass.example
      </li>
    </ul>

    <div class="social-links" aria-label="Social profiles">
      <span class="social-slot"></span>
      <span class="social-slot"></span>
      <span class="social-slot"></span>
    </div>
  </div>
</body>
</html>
```